Napa Winery - Chardonnay wine label

We are looking for a label for a new Napa Valley winery - chardonnay wine. The winery is "Harrowgate Ridge Vintners" and we would like to see it depicted on a white wine (chardonnay style) bottle. The winery is called Harrowgate Ridge Vintners.

We are open to ideas!

Target Market(s)

High-end chardonnay lovers

Requirements
Nice to have
• Painted or etched label onto bottle

```html
<!DOCTYPE html>
<html lang="en">
<head>
<meta charset="utf-8">
<title>Harrowgate Ridge Vintners – Chardonnay Label</title>
<link rel="stylesheet" href="https://fonts.googleapis.com/css2?family=Archivo:wght@500;700&family=Cormorant+Garamond:wght@600&display=swap">
<style>
  :root {
    --page-bg: #ffffff;
    --label-bg: #ffffff;
    --label-border: #c9c9c9;
    --band-grey: #bdbec1;
    --gold: #a98b2c;
    --white: #ffffff;
    --photo-dark: #3c3c3c;
    --photo-mid: #8e8e8e;
    --photo-light: #e6e6e6;
  }
  * { margin: 0; padding: 0; box-sizing: border-box; }
  html, body {
    width: 924px;
    height: 1200px;
    overflow: hidden;
    background: var(--page-bg);
  }
  .canvas {
    position: relative;
    width: 924px;
    height: 1200px;
    background: var(--page-bg);
  }
  .wine-label {
    position: absolute;
    left: 154px;
    top: 45px;
    width: 616px;
    height: 1110px;
    background: var(--label-bg);
    border: 2px solid var(--label-border);
    font-family: "Archivo", Arial, sans-serif;
  }
  .estate-vignette {
    position: absolute;
    left: 93px;
    top: 46px;
    width: 413px;
    height: 157px;
    display: block;
  }
  .brand-name {
    position: absolute;
    left: 38px;
    top: 300px;
    font-family: "Cormorant Garamond", Georgia, serif;
    font-weight: 600;
    font-size: 47px;
    letter-spacing: 2px;
    color: var(--gold);
    white-space: nowrap;
    line-height: 1;
  }
  .varietal-band {
    position: absolute;
    left: 0;
    top: 378px;
    width: 100%;
    height: 64px;
    background: var(--band-grey);
    display: flex;
    align-items: center;
    justify-content: center;
  }
  .varietal {
    font-weight: 700;
    font-size: 24px;
    letter-spacing: 8px;
    color: var(--white);
    padding-left: 8px;
  }
  .vintage-block {
    position: absolute;
    left: 0;
    top: 1005px;
    width: 100%;
    text-align: center;
    color: var(--gold);
    font-weight: 700;
    line-height: 1;
  }
  .vintage {
    font-size: 50px;
    letter-spacing: 2px;
  }
  .appellation {
    margin-top: 12px;
    font-size: 28px;
    letter-spacing: 2px;
  }
</style>
</head>
<body>
  <main class="canvas">
    <section class="wine-label">
      <svg class="estate-vignette" viewBox="0 0 413 157" role="img" aria-label="Black and white photograph of a stone wine cave entrance among vineyard trees, in an oval vignette">
        <defs>
          <radialGradient id="vignette-tone" cx="50%" cy="45%" r="55%">
            <stop offset="0%" stop-color="#8e8e8e"/>
            <stop offset="55%" stop-color="#3c3c3c"/>
            <stop offset="85%" stop-color="#8e8e8e"/>
            <stop offset="100%" stop-color="#e6e6e6"/>
          </radialGradient>
        </defs>
        <ellipse cx="206.5" cy="78.5" rx="206.5" ry="78.5" fill="url(#vignette-tone)"/>
      </svg>

      <h1 class="brand-name">HARROWGATE RIDGE</h1>

      <div class="varietal-band">
        <p class="varietal">CHARDONNAY</p>
      </div>

      <div class="vintage-block">
        <p class="vintage">2014</p>
        <p class="appellation">NAPA VALLEY</p>
      </div>
    </section>
  </main>
</body>
</html>
```